We need a flyer for our company. We test drugs, laser, LED or other light sources for phototoxicity on healthy volunteers.
You can use our website for an idea or imagine www.lumivanta.co.uk
Lumivanta has a well-established reputation in the field of drug- and chemical-induced phototoxicity and expertise in clinical studies of photoprotective agents, such as nutraceuticals and antioxidants and light-based device development and application. The team at Lumivanta has an international reputation in the field of UV and visible light measurement and our team has a truly multidisciplinary nature, with professionals including physicians, medical physicists, biochemists, technicians and nurses.

Target Market(s)

any pharmaceutical or cosmetical company

Industry/Entity Type

Cosmetic

Font styles to use
Serif

Colors

Designer to choose colors to be used in the design.

Requirements
Must have
• Clinical studies:
• Phototoxicity
• Photoallergy to topical agents
• Photoprotection by oral or topical agents
• Light-based devices
• Laboratory studies:
• Photosafety and photoxicity
• Photophysics and light source evaluation
Nice to have
• Can you reduce the amount of text and concentrate on this point?
• First page:
• • Lumivanta has a well-established reputation in the field of drug- and chemical-induced phototoxicity and expertise in clinical studies of photoprotective agents:
• such as nutraceuticals
• and antioxidants
• and light-based device development and application.
• • The team at Lumivanta has an international reputation in the field of UV and visible light measurement and our team has a truly multidisciplinary nature, with professionals including physicians, medical physicists, biochemists, technicians and nurses
• Second page:
• Clinical studies
• Phototoxicity
• Light-based devices
• Laboratory studies

```html
<!DOCTYPE html>
<html lang="en">
<head>
<meta charset="utf-8">
<title>Lumivanta Flyer</title>
<link rel="stylesheet" href="https://fonts.googleapis.com/css2?family=Roboto:wght@400;500;700;900&display=swap">
<style>
  :root {
    --blue: #1547b3;
    --blue-deep: #0d3590;
    --blue-light: #86a8ec;
    --blue-pale: #dce7fb;
    --ink: #1d1f24;
    --paper: #ffffff;
    --stage: #2c2f34;
  }
  * { box-sizing: border-box; margin: 0; padding: 0; }
  html, body { width: 1200px; height: 1200px; overflow: hidden; }
  body { background: var(--stage); font-family: "Roboto", Arial, sans-serif; color: var(--ink); position: relative; }

  .page { position: absolute; top: 204px; width: 560px; height: 792px; background: var(--paper); overflow: hidden; }
  .page--front { left: 30px; }
  .page--back { left: 610px; }
  .abs { position: absolute; }

  /* front */
  .front-header { left: 0; top: 0; width: 100%; height: 78px; background: var(--blue); display: flex; align-items: center; justify-content: center; gap: 12px; }
  .brand-mark { width: 30px; height: 30px; background: var(--paper); }
  .brand-name { color: var(--paper); font-weight: 700; font-size: 30px; letter-spacing: .5px; }
  .hero-photo { left: 0; top: 78px; width: 100%; height: 370px; background: linear-gradient(90deg, #eef5f4 0%, #d3e8e6 35%, #7fb8b4 65%, #46807f 100%); }
  .hero-wave { left: 0; top: 370px; width: 560px; height: 90px; }
  .headline { left: 36px; top: 112px; font-weight: 900; font-size: 39px; line-height: 45px; text-transform: uppercase; color: var(--ink); }
  .headline .accent { color: var(--blue); }
  .tagline { left: 50px; top: 440px; font-weight: 500; font-size: 23px; color: var(--blue); transform: rotate(-3deg); transform-origin: left; white-space: nowrap; }
  .tagline b { font-size: 30px; font-weight: 700; color: var(--blue-light); }
  .body-col { font-size: 8.6px; line-height: 13px; color: var(--ink); width: 215px; transform: rotate(-3deg); transform-origin: left top; text-align: justify; }
  .body-col--left { left: 50px; top: 510px; }
  .body-col--right { left: 300px; top: 490px; width: 210px; }
  .bullets { left: 52px; top: 572px; font-size: 8.6px; line-height: 14px; list-style: none; transform: rotate(-3deg); transform-origin: left top; }
  .bullets li::before { content: ""; display: inline-block; width: 4px; height: 4px; border-radius: 50%; background: var(--ink); margin-right: 7px; vertical-align: middle; }
  .photo-circle { border-radius: 50%; border: 5px solid var(--blue-light); }
  .photo-circle--uv { left: 318px; top: 588px; width: 112px; height: 112px; background: radial-gradient(circle at 55% 45%, #6f7fe0, #1c2a66 60%, #0d1230); z-index: 2; }
  .photo-circle--camera { left: 412px; top: 604px; width: 140px; height: 140px; background: radial-gradient(circle at 50% 45%, #a9a59e, #5c5852 55%, #2a2826); z-index: 3; }
  .front-footer { left: 0; top: 620px; width: 560px; height: 172px; }
  .contact-title { font-weight: 700; font-size: 22px; color: var(--paper); }
  .contact-line { display: flex; align-items: center; gap: 5px; font-size: 13px; color: var(--paper); }
  .contact-line svg { width: 13px; height: 13px; flex: none; }
  .front-contact-title { left: 46px; top: 716px; transform: rotate(-3deg); }
  .front-phone { left: 46px; top: 752px; transform: rotate(-3deg); }
  .front-web { left: 220px; top: 716px; transform: rotate(-3deg); }
  .front-mail { left: 222px; top: 740px; transform: rotate(-3deg); }

  /* back */
  .section-pill { background: var(--blue-light); color: var(--paper); font-size: 21px; padding: 5px 14px; border-radius: 3px; white-space: nowrap; }
  .pill-clinical { left: 190px; top: 28px; }
  .pill-lab { left: 18px; top: 352px; background: #7fa0e4; }
  .study { display: flex; gap: 10px; width: 250px; }
  .study-photo { flex: none; width: 96px; height: 76px; border-radius: 50%; border: 3px solid var(--blue); }
  .study-text { min-width: 0; flex: 1; }
  .study-text h3 { font-size: 9.5px; font-weight: 500; color: var(--blue); margin: 4px 0 4px; }
  .study-text p { font-size: 6.6px; line-height: 8.6px; text-align: justify; }
  .study--lab .study-photo { width: 110px; height: 92px; border-color: var(--blue-light); }
  .study--lab h3 { color: var(--blue-pale); font-size: 10px; }
  .study--lab p { color: var(--blue-pale); }
  .s-tox { left: 24px; top: 88px; }
  .s-tox .study-photo { background: linear-gradient(135deg, #cfd5dc, #7d8792); }
  .s-allergy { left: 292px; top: 68px; width: 254px; }
  .s-allergy .study-photo { background: linear-gradient(135deg, #e2e8ee, #8e9aa6); }
  .s-protect { left: 24px; top: 218px; }
  .s-protect .study-photo { background: linear-gradient(135deg, #f1f4f7, #b5c0ca); }
  .s-device { left: 292px; top: 198px; width: 254px; }
  .s-device .study-photo { background: radial-gradient(circle at 50% 50%, #6b5f3e, #1f1c14 70%); }
  .back-band { left: 0; top: 300px; width: 560px; height: 380px; }
  .s-safety { left: 20px; top: 430px; width: 262px; }
  .s-safety .study-photo { background: linear-gradient(160deg, #c4a6e8, #7d4fbf 55%, #3b2a6e); }
  .s-physics { left: 292px; top: 410px; width: 258px; }
  .s-physics .study-photo { background: radial-gradient(circle at 45% 50%, #f1a64a, #6b3b14 45%, #101424 80%); }
  .back-contact .contact-title, .back-contact.contact-title { color: var(--blue); }
  .back-contact.contact-line { color: var(--blue-deep); }
  .back-contact-title { left: 60px; top: 690px; }
  .back-phone { left: 60px; top: 730px; }
  .back-web { left: 300px; top: 690px; }
  .back-mail { left: 300px; top: 714px; }
  .back-base { left: 0; top: 780px; width: 100%; height: 12px; background: var(--blue-light); }
</style>
</head>
<body>

<section class="page page--front">
  <header class="abs front-header">
    <span class="brand-mark"></span>
    <span class="brand-name">Lumivanta</span>
  </header>
  <div class="abs hero-photo" role="img" aria-label="Clinical staff in scrubs and lab coats talking in a bright hospital corridor"></div>
  <svg class="abs hero-wave" viewBox="0 0 560 90" preserveAspectRatio="none">
    <path d="M0 40 C150 10 380 0 560 30 L560 90 L0 90 Z" fill="#ffffff"/>
  </svg>
  <h1 class="abs headline">Your<br><span class="accent">Health</span><br>Is Our<br>Main<br><span class="accent">Priority</span></h1>

  <h2 class="abs tagline">We Provide The <b>Best</b> Medical Service</h2>
  <p class="abs body-col body-col--left">Lumivanta has a well-established reputation in the field of drug- and chemical-induced phototoxicity and expertise in clinical studies of photoprotective agents:</p>
  <p class="abs body-col body-col--right">The team at Lumivanta has an international reputation in the field of UV and visible light measurement and our team has a truly multidisciplinary nature, with professionals including physicians, medical physicists, biochemists, technicians and nurses.</p>
  <ul class="abs bullets">
    <li>Such as nutraceuticals</li>
    <li>Antioxidants</li>
    <li>Light-based device development and application</li>
  </ul>

  <svg class="abs front-footer" viewBox="0 0 560 172" preserveAspectRatio="none">
    <path d="M0 70 C160 20 330 30 560 50 L560 172 L0 172 Z" fill="#86a8ec"/>
    <path d="M0 78 C160 28 330 38 560 58 L560 172 L0 172 Z" fill="#1547b3"/>
  </svg>
  <div class="abs photo-circle photo-circle--uv" role="img" aria-label="Laboratory bench lit by blue ultraviolet lamps"></div>
  <div class="abs photo-circle photo-circle--camera" role="img" aria-label="Hand holding a thermal imaging camera"></div>

  <div class="abs contact-title front-contact-title">Contact Us</div>
  <div class="abs contact-line front-phone">
    <svg viewBox="0 0 16 16"><circle cx="8" cy="8" r="7" fill="none" stroke="#fff" stroke-width="1.3"/><path d="M5 4.5 L6.5 4.5 L7 6.5 L6 7.2 C6.6 8.6 7.4 9.4 8.8 10 L9.5 9 L11.5 9.5 L11.5 11 C8 11.5 4.5 8 5 4.5 Z" fill="#fff"/></svg>
    01632 960418
  </div>
  <div class="abs contact-line front-web">
    <svg viewBox="0 0 16 16" fill="none" stroke="#fff" stroke-width="1.2"><circle cx="8" cy="8" r="6.5"/><ellipse cx="8" cy="8" rx="3" ry="6.5"/><path d="M1.5 8 H14.5 M2.5 5 H13.5 M2.5 11 H13.5"/></svg>
    www.lumivanta.co.uk
  </div>
  <div class="abs contact-line front-mail">
    <svg viewBox="0 0 16 16"><circle cx="8" cy="8" r="7" fill="none" stroke="#fff" stroke-width="1.3"/><rect x="4" y="5.5" width="8" height="5.5" fill="#fff"/><path d="M4 5.5 L8 8.5 L12 5.5" fill="none" stroke="#1547b3" stroke-width="1"/></svg>
    info@lumivanta.co.uk
  </div>
</section>

<section class="page page--back">
  <div class="abs section-pill pill-clinical">Clinical Studies</div>

  <article class="abs study s-tox">
    <div class="study-photo" role="img" aria-label="Monitor displaying clinical test results"></div>
    <div class="study-text"><h3>Phototoxicity</h3><p>Our clinical studies test whether a drug, laser, LED or other light source can cause phototoxicity in volunteers.</p></div>
  </article>
  <article class="abs study s-allergy">
    <div class="study-photo" role="img" aria-label="Clinical room with light testing equipment"></div>
    <div class="study-text"><h3>Photoallergy to Topical Agents</h3><p>Some drugs and chemicals that absorb UV or visible light may trigger photoallergy when applied to the skin.</p></div>
  </article>
  <article class="abs study s-protect">
    <div class="study-photo" role="img" aria-label="Glass laboratory flasks on a bench"></div>
    <div class="study-text"><h3>Photoprotection by Oral<br>or Topical Agents</h3><p>We run healthy volunteer studies of photoprotective compounds, such as nutraceuticals and antioxidants, given orally or topically.</p></div>
  </article>
  <article class="abs study s-device">
    <div class="study-photo" role="img" aria-label="Light-based device under dim lighting"></div>
    <div class="study-text"><h3>Light-Based Devices</h3><p>We assess and clinically trial light-based diagnostic and therapeutic devices with dedicated photophysicists.</p></div>
  </article>

  <svg class="abs back-band" viewBox="0 0 560 380" preserveAspectRatio="none">
    <path d="M0 45 C90 0 200 -5 330 20 C440 40 520 20 560 0 L560 190 C520 330 330 250 180 280 C90 300 30 340 0 370 Z" fill="#86a8ec"/>
    <path d="M0 52 C90 8 200 3 330 28 C440 48 520 28 560 8 L560 190 C520 320 330 240 180 272 C90 292 30 332 0 362 Z" fill="#1547b3"/>
  </svg>
  <div class="abs section-pill pill-lab">Laboratory Studies</div>

  <article class="abs study study--lab s-safety">
    <div class="study-photo" role="img" aria-label="Cell culture well plate glowing purple"></div>
    <div class="study-text"><h3>Photosafety and Photoxicity</h3><p>Our team performs in vitro photoxicity studies of investigational compounds in human cell cultures, following current regulatory guidelines.</p></div>
  </article>
  <article class="abs study study--lab s-physics">
    <div class="study-photo" role="img" aria-label="Light source glowing inside a measurement chamber"></div>
    <div class="study-text"><h3>Photophysics and Light<br>Source Evaluation</h3><p>We place high value on accurate dosimetry, the science of measurement. In one word: confidence.</p></div>
  </article>

  <div class="abs contact-title back-contact back-contact-title">Contact Us</div>
  <div class="abs contact-line back-contact back-phone">
    <svg viewBox="0 0 16 16"><circle cx="8" cy="8" r="7" fill="none" stroke="#0d3590" stroke-width="1.3"/><path d="M5 4.5 L6.5 4.5 L7 6.5 L6 7.2 C6.6 8.6 7.4 9.4 8.8 10 L9.5 9 L11.5 9.5 L11.5 11 C8 11.5 4.5 8 5 4.5 Z" fill="#0d3590"/></svg>
    01632 960418
  </div>
  <div class="abs contact-line back-contact back-web">
    <svg viewBox="0 0 16 16" fill="none" stroke="#0d3590" stroke-width="1.2"><circle cx="8" cy="8" r="6.5"/><ellipse cx="8" cy="8" rx="3" ry="6.5"/><path d="M1.5 8 H14.5 M2.5 5 H13.5 M2.5 11 H13.5"/></svg>
    www.lumivanta.co.uk
  </div>
  <div class="abs contact-line back-contact back-mail">
    <svg viewBox="0 0 16 16"><circle cx="8" cy="8" r="7" fill="none" stroke="#0d3590" stroke-width="1.3"/><rect x="4" y="5.5" width="8" height="5.5" fill="#0d3590"/><path d="M4 5.5 L8 8.5 L12 5.5" fill="none" stroke="#fff" stroke-width="1"/></svg>
    info@lumivanta.co.uk
  </div>
  <div class="abs back-base"></div>
</section>

</body>
</html>
```